Leading Nutrition Company Needs a Stylish Label Design!

We need a label/packaging design for our new cutting-edge detox called "Clear Tide". It is an all organic detox that removes toxins, harsh-chemicals, herbicides, pesticides and heavy metals from the body. It essentially turns everything you eat into organic whole foods and without all the chemicals in our bodies, we run at optimal performance.

We are attempting to blend a modern, simplistic design for our label.
We would like to see designs that use flat grays, silvers and blacks. We would also like to see pops of green and or blue in the design. Overall design will be a modern, contemporary matte finish with pops of color in either a pattern design or colored lettering. The final design should convey a high-end, exclusive health product.

Target Market(s)

Health conscious individuals and those seeking to pass an upcoming drug test. Athletes, nutritionist, dietitians ranging from 18-70 years of age.

Industry/Entity Type

Health

Font styles to use
Other font styles liked:
• Unique modern fonts

Colors
b1b1b1
9d9d9d
474747
33a6d7
0192cd
9ccb3b

Requirements
Must have
• Must be modern and simplistic

Pops of color - Don't need to be matte

Matte finishes for background
-Light grays, graphite, light silvers etc

Lettering must be modern and unique

Label type wil be a "shrink label" for an 8 oz boston squat bottle
-See attached link for bottle

"Clear Tide" some where on label

Company logo some where on label
-See attached files for logo
Nice to have
• Cool background designs that provide depth to the design.

A strip of pattern design running vertically or horizontally to capture the eye.
-See attached pictures for examples
Should not have
• Script or Normal fonts

```html
<!DOCTYPE html>
<html lang="en">
<head>
<meta charset="utf-8">
<title>Clear Tide Label</title>
<link href="https://fonts.googleapis.com/css2?family=Josefin+Sans:wght@200;400&family=Playfair+Display:wght@700&display=swap" rel="stylesheet">
<style>
  :root {
    --stage: #e4e6e3;
    --label-green: #a4c83a;
    --ink-white: #f4f7ec;
    --graphite: #4f5459;
    --rule-gray: #6b6f73;
  }
  html, body {
    margin: 0;
    width: 1200px;
    height: 1000px;
    overflow: hidden;
    background: var(--stage);
  }
  .canvas {
    position: relative;
    width: 1200px;
    height: 1000px;
  }
  .label {
    position: absolute;
    left: 220px;
    top: 40px;
    width: 760px;
    height: 920px;
    background: var(--label-green);
  }
  .rule-top {
    position: absolute;
    left: 0; right: 0;
    top: 50px;
    height: 6px;
    background: var(--ink-white);
  }
  .rule-bottom {
    position: absolute;
    left: 0; right: 0;
    top: 872px;
    height: 6px;
    background: var(--rule-gray);
  }
  .brand {
    position: absolute;
    top: 92px;
    left: 0; right: 0;
    display: flex;
    flex-direction: column;
    align-items: center;
    gap: 8px;
  }
  .brand-dot {
    width: 38px;
    height: 38px;
    border-radius: 50%;
    background: var(--graphite);
  }
  .brand-name {
    font-family: "Josefin Sans", sans-serif;
    font-weight: 400;
    font-size: 20px;
    letter-spacing: 1px;
    color: var(--graphite);
  }
  .title-frame {
    position: absolute;
    left: 215px;
    top: 232px;
    width: 330px;
    height: 610px;
    box-sizing: border-box;
    border: 5px solid var(--ink-white);
    display: flex;
    flex-direction: column;
    align-items: center;
    color: var(--ink-white);
    overflow: hidden;
  }
  .title-line {
    font-family: "Josefin Sans", sans-serif;
    font-weight: 200;
    line-height: 1;
    white-space: nowrap;
  }
  .title-line.first {
    margin-top: 42px;
    font-size: 84px;
    letter-spacing: 1px;
  }
  .title-initial {
    font-family: "Playfair Display", serif;
    font-weight: 700;
    font-size: 240px;
    line-height: 0.95;
    margin: 10px 0 0;
  }
  .title-line.last {
    margin-top: 8px;
    font-size: 96px;
    letter-spacing: 2px;
  }
  .emblem {
    margin-top: auto;
    margin-bottom: 30px;
    width: 90px;
    height: 46px;
    border-radius: 50% 50% 8px 8px;
    background: rgba(244, 247, 236, 0.85);
  }
</style>
</head>
<body>
  <div class="canvas">
    <div class="label">
      <div class="rule-top"></div>
      <div class="brand">
        <div class="brand-dot"></div>
        <div class="brand-name">Verdant Labs</div>
      </div>
      <div class="title-frame">
        <div class="title-line first">CLEAR</div>
        <div class="title-initial">T</div>
        <div class="title-line last">IDE</div>
        <div class="emblem" role="img" aria-label="Small lotus leaf emblem"></div>
      </div>
      <div class="rule-bottom"></div>
    </div>
  </div>
</body>
</html>
```